Offshore Energy Projects Management Consultancy needs a business card design

Logo available. We provide teams to deliver engineering consultancy, project management and delivery teams mainly in the offshore renewables sector. The company is all about bringing the right people to a project to deliver the scope.

The business card will be used for all staff.

The business card should be quite simple, vibrant and uncluttered but convey experience, enthusiasm and integration.

Target Market(s)

Energy Project Developers and Tier 1 construction companies

Contact Information for Business Card

Logo should be on the back of the card. I'm happy for the designer to play with the colour of the logo and background colour.

Front of the card should convey all the must have information in a clear and professional manner but without being overly traditional.

Colors

Designer to choose colors to be used in the design.

Requirements
Must have
• Land Line Tel Number, Mobile Tel Number, Email, business address, web address.

```html
<!DOCTYPE html>
<html lang="en">
<head>
<meta charset="utf-8">
<title>Tidewater Delivery Group – Business Card</title>
<link rel="stylesheet" href="https://fonts.googleapis.com/css2?family=Questrial&family=Kanit:wght@500&display=swap">
<style>
  :root {
    --page-bg: #e6e8ea;
    --card-bg: #ffffff;
    --blue-deep: #1b75bb;
    --blue-bright: #29a9e0;
    --ink-grey: #6d6e70;
  }
  * { box-sizing: border-box; margin: 0; padding: 0; }
  html, body { width: 1200px; height: 1200px; overflow: hidden; }
  body {
    background: var(--page-bg);
    font-family: "Questrial", sans-serif;
    position: relative;
  }
  .card {
    position: absolute;
    left: 216px;
    width: 766px;
    height: 446px;
    background: var(--card-bg);
    overflow: hidden;
  }
  .card--back { top: 108px; }
  .card--front { top: 631px; }

  .chain-band {
    position: absolute;
    left: 0; right: 0;
    top: 338px;
    height: 104px;
    background: linear-gradient(180deg, var(--blue-deep) 0%, var(--blue-bright) 100%);
    opacity: .85;
  }
  .chain-column {
    position: absolute;
    top: 0; bottom: 0;
    left: 22px;
    width: 103px;
    background: linear-gradient(90deg, var(--blue-deep) 0%, var(--blue-bright) 100%);
    opacity: .85;
  }

  .brand {
    position: absolute;
    right: 28px;
    top: 190px;
    display: flex;
    align-items: center;
    gap: 14px;
  }
  .brand__mark {
    width: 26px; height: 26px;
    background: var(--blue-deep);
    flex: none;
  }
  .brand__name {
    font-family: "Questrial", sans-serif;
    font-size: 29px;
    color: var(--ink-grey);
    letter-spacing: .5px;
    line-height: 1.1;
  }

  .contact-list {
    position: absolute;
    left: 383px;
    top: 0;
    list-style: none;
  }
  .contact-item {
    position: absolute;
    left: 0;
    display: flex;
    align-items: center;
    white-space: nowrap;
  }
  .contact-item--phone { top: 88px; }
  .contact-item--mobile { top: 140px; }
  .contact-item--email { top: 193px; }
  .contact-item--web { top: 244px; }
  .contact-item--address { top: 298px; }
  .contact-icon {
    width: 49px; height: 48px;
    border-radius: 14px;
    background: var(--blue-deep);
    display: flex; align-items: center; justify-content: center;
    flex: none;
  }
  .contact-icon svg { width: 30px; height: 30px; }
  .contact-text {
    margin-left: 26px;
    font-size: 21px;
    color: var(--ink-grey);
    line-height: 1.3;
  }
  .contact-text--number {
    font-family: "Kanit", sans-serif;
    font-weight: 500;
    font-size: 22px;
    letter-spacing: .3px;
  }
  .contact-text--address { word-spacing: 3px; }
</style>
</head>
<body>

<section class="card card--back">
  <div class="brand">
    <span class="brand__mark"></span>
    <span class="brand__name">TIDEWATER<br>DELIVERY GROUP</span>
  </div>
  <div class="chain-band" role="img" aria-label="Band of interlinked blue chain links"></div>
</section>

<section class="card card--front">
  <div class="chain-column" role="img" aria-label="Vertical column of interlinked blue chain links"></div>

  <ul class="contact-list">
    <li class="contact-item contact-item--phone">
      <span class="contact-icon">
        <svg viewBox="0 0 30 30" fill="#fff" aria-hidden="true">
          <path d="M3 10c0-3 6-5 12-5s12 2 12 5v2h-6v-3h-12v3h-6z"/>
          <rect x="7" y="13" width="16" height="12" rx="3"/>
        </svg>
      </span>
      <span class="contact-text contact-text--number">+44 1224 555 018</span>
    </li>
    <li class="contact-item contact-item--mobile">
      <span class="contact-icon">
        <svg viewBox="0 0 30 30" fill="none" stroke="#fff" stroke-width="2" aria-hidden="true">
          <rect x="9" y="3" width="12" height="24" rx="2"/>
          <line x1="13" y1="23" x2="17" y2="23"/>
        </svg>
      </span>
      <span class="contact-text contact-text--number">+44 7700 900 214</span>
    </li>
    <li class="contact-item contact-item--email">
      <span class="contact-icon">
        <svg viewBox="0 0 30 30" fill="none" stroke="#fff" stroke-width="2" aria-hidden="true">
          <rect x="4" y="7" width="22" height="16" rx="1"/>
          <path d="M4 8l11 9 11-9"/>
        </svg>
      </span>
      <span class="contact-text">hello@tidewaterdg.com</span>
    </li>
    <li class="contact-item contact-item--web">
      <span class="contact-icon">
        <svg viewBox="0 0 30 30" fill="none" stroke="#fff" stroke-width="2" aria-hidden="true">
          <circle cx="15" cy="15" r="11"/>
          <ellipse cx="15" cy="15" rx="5" ry="11"/>
          <line x1="4" y1="15" x2="26" y2="15"/>
        </svg>
      </span>
      <span class="contact-text">www.tidewaterdg.com</span>
    </li>
    <li class="contact-item contact-item--address">
      <span class="contact-icon">
        <svg viewBox="0 0 30 30" fill="none" stroke="#fff" stroke-width="2" aria-hidden="true">
          <path d="M15 27s-8-8-8-14a8 8 0 0 1 16 0c0 6-8 14-8 14z"/>
          <circle cx="15" cy="13" r="3"/>
        </svg>
      </span>
      <span class="contact-text contact-text--address">TDG House, 14 Quay Road,<br>Harbourton, HT4 2QD</span>
    </li>
  </ul>
</section>

</body>
</html>
```